Redesign of www.tidewellgallerynews.example.

I need to take the elements of a PixelHive website that was started some time ago but never went live with a website that I now have that is not very compelling. I publish a digital magazine through pagereel.example and link the magazine to www.tidewellgallerynews.example. Boring website.

The PixelHive website is: www.coveharborfunandshows.example. A lively website which is now too narrow in scope. I seek to expand my coverage to include the cultural life of my county.

Here's what I'd like to do.
1. Rename the PixelHive website using my url: www.tidewellgallerynews.example.
2. Use my tidewellgallerynews logo, replacing coveharborfunandshows.example
3. Break up the large rotating banner on the top into two spaces??? I want to feature my current magazine as the first placement. The space is too wide? Suggestions here appreciated. I also want back issues to be available for viewing.
4. I need flexibility to change headings, etc, so instruction needs to come with the design.
5. I'm thinking of offering blog space to others.

General question. Rather than moving everything over to www.coveharborfunandshows.example, should we just redesign www.tidewellgallerynews.example using the elements on the www.coveharborfunandshows.example site? Might be an easier way to go.

I'm open to a complete redesign of www.tidewellgallerynews.example with the exception of the logo and the spotlight on the magazines,both current and past issues.

I am in the middle of producing the next issue, so the website needs to not change until mid October. I'd like the design to be complete beforehand so we can make the change pretty quickly after the 15th of October.

I've attached covers of our last 2 issues and my logo. I'm open to a change in color with the logo,but not the fonts.

I'm not sure how many pages I'll need and I don't know the difference between coded and uncoded pages...so you can explain to me.

Target Market(s)

Readers who are interested in the arts and culture of the San Francisco Bay Area.

Number of Pages Required

4 page

Font styles to use
Other font styles liked:
• Whatever font is used at www.coveharborfunandshows.example

Colors

Designer to choose colors to be used in the design.

Requirements
Must have
• Current logo. Color suggestion for the website is fine.Featured space for the magazines. They are placed by my linking them from Pagereel.example over to my current website. www.coveharborfunandshows should be used as a template.
• WordPress for blogging and instructions included.
Nice to have
• Nice, bright, fun

```html
<!DOCTYPE html>
<html lang="en">
<head>
<meta charset="utf-8">
<title>Tidewell Gallery News</title>
<link href="https://fonts.googleapis.com/css2?family=Questrial&family=Raleway:wght@400;500&display=swap" rel="stylesheet">
<style>
:root{
  --green:#7fcc98;
  --green-dark:#5fb77d;
  --coral:#fb5a43;
  --navy:#2b5a86;
  --ink:#222;
  --muted:#7a7a7a;
  --rule:#d9d9d9;
  --footer-bar:#4b4b4b;
  --white:#fff;
}
*{box-sizing:border-box;margin:0;padding:0}
html,body{width:1200px;height:2894px;overflow:hidden;background:var(--white)}
body{position:relative;font-family:"Questrial",sans-serif;color:var(--ink)}
h1,h2,h3{font-weight:400}
.abs{position:absolute}

/* header */
.site-header{left:0;top:0;width:1200px;height:102px;display:flex;align-items:center;justify-content:center;gap:12px}
.brand-dot{width:14px;height:14px;border-radius:50%;background:var(--green)}
.brand-name{font-size:30px;color:var(--navy);letter-spacing:.5px}

.main-nav{left:0;top:102px;width:1200px;height:52px;background:var(--green);display:flex;align-items:center;justify-content:center}
.main-nav a{color:var(--white);text-decoration:none;font-size:14px;letter-spacing:.6px;padding:0 36px;border-left:1px solid rgba(255,255,255,.6);line-height:14px}
.main-nav a:first-child{border-left:0}

/* hero issues */
.hero-issue{top:164px;height:473px}
.hero-issue.current{left:0;width:594px;background:linear-gradient(160deg,#a9cbe6 0%,#7fa6c4 45%,#3c4a57 100%)}
.hero-issue.premiere{left:604px;width:596px;background:linear-gradient(160deg,#d8d8d8 0%,#8a8a8a 50%,#2e2e2e 100%)}
.read-now{position:absolute;left:85px;top:324px;width:195px;height:66px;background:rgba(70,70,70,.55);color:var(--white);font-size:26px;letter-spacing:1px;display:flex;align-items:center;justify-content:center}
.hero-issue.premiere .read-now{left:79px}
.slider-dots{left:0;top:665px;width:1200px;display:flex;justify-content:center;gap:12px}
.slider-dots span{width:15px;height:15px;border-radius:50%;background:#cfcfcf}
.slider-dots span.active{background:var(--green)}

/* back issues */
.back-issue{top:710px;width:324px;height:230px}
.issue-a{left:85px;background:linear-gradient(150deg,#e4e4e4,#6f6f6f 60%,#2a2a2a)}
.issue-b{left:436px;background:linear-gradient(150deg,#4a3c35,#8b5a45 55%,#c9a58a)}
.issue-c{left:787px;background:linear-gradient(150deg,#2e8fcf,#3b6fb0 50%,#e58a3a)}
.btn{display:flex;align-items:center;justify-content:center;background:var(--coral);color:var(--white);text-transform:uppercase;font-size:13px;letter-spacing:.4px}
.view-all{left:513px;top:986px;width:174px;height:50px;font-size:14px}

/* section labels */
.label{display:flex;align-items:center;background:var(--green);color:var(--white);font-size:13px;padding:0 14px;height:29px;text-transform:uppercase}
.label-rule{height:1px;background:var(--green)}

/* posts */
.post-card{border:1px solid var(--rule);background:var(--white)}
.post-image{position:absolute;left:0;top:0;width:100%}
.post-title{position:absolute;font-size:20px;font-weight:400;text-transform:uppercase;color:var(--ink)}
.post-meta{position:absolute;font-size:11px;color:var(--coral);font-style:italic;display:flex;gap:18px}
.post-excerpt{position:absolute;font-size:12.5px;line-height:20px;color:var(--muted)}
.post-card .btn{position:absolute}

.feature-post{left:85px;top:1119px;width:677px;height:507px}
.feature-post .post-image{height:262px;background:linear-gradient(180deg,#6d6d6d,#bdbdbd 45%,#e8e8e8 70%,#4b4b4b)}
.feature-post .post-title{left:30px;top:338px}
.feature-post .post-meta{left:30px;top:372px}
.feature-post .post-excerpt{left:30px;top:400px;width:620px}
.feature-post .btn{left:30px;top:448px;width:112px;height:36px}

.small-post{top:1671px;width:324px;height:490px}
.small-post.one{left:85px}
.small-post.two{left:436px}
.small-post .post-image{height:279px}
.small-post.one .post-image{background:linear-gradient(180deg,#2d4f55,#a7c3c4 55%,#6f8f3a)}
.small-post.two .post-image{background:linear-gradient(180deg,#1d7fd0,#78b8e8 55%,#2aa2b8)}
.small-post .post-title{left:16px;top:306px;font-size:16.5px}
.small-post .post-meta{left:16px;top:333px}
.small-post .post-excerpt{left:16px;top:364px;width:292px;height:40px;overflow:hidden;font-size:12px}
.small-post .btn{left:22px;top:426px;width:108px;height:35px;font-size:12px}

/* about panel */
.about-panel{left:787px;top:1067px;width:324px;height:559px;border:1px solid var(--rule)}
.about-panel .label{position:absolute;left:20px;top:18px}
.about-panel .label-rule{position:absolute;left:20px;top:46px;width:284px}
.about-photo{left:49px;top:83px;width:224px;height:224px;border-radius:50%;background:radial-gradient(circle at 50% 45%,#e9d9cf,#c7b3a6 70%,#efe9e4)}
.about-text{left:20px;top:350px;width:284px;text-align:center;font-size:13px;line-height:23px;color:var(--ink)}
.outline-btn{left:97px;top:434px;width:125px;height:37px;border:1px solid var(--coral);color:var(--coral);font-size:13px;display:flex;align-items:center;justify-content:center;text-transform:uppercase}
.about-social{left:0;top:504px;width:322px;display:flex;justify-content:center;gap:28px}
.about-social span{width:14px;height:14px;border-radius:50%;background:var(--coral)}

/* newsletter */
.newsletter{left:787px;top:1671px;width:324px;height:490px;background:linear-gradient(160deg,#3b2d24,#2a211b 50%,#4a3a2d)}
.newsletter-frame{position:absolute;left:27px;top:27px;width:270px;height:436px;border:1px solid rgba(255,255,255,.6)}
.newsletter-title{position:absolute;left:0;top:56px;width:324px;text-align:center;color:var(--white);font-size:27px;font-weight:400;line-height:47px;text-transform:uppercase}
.newsletter-rule{position:absolute;left:137px;top:181px;width:50px;height:1px;background:var(--white)}
.newsletter-text{position:absolute;left:50px;top:210px;width:224px;text-align:center;color:var(--white);font-size:13px;line-height:20px}
.email-field{position:absolute;left:44px;top:295px;width:234px;height:50px;background:var(--white);color:#999;font-size:12px;display:flex;align-items:center;padding-left:14px}
.newsletter .btn{position:absolute;left:44px;top:364px;width:234px;height:52px;font-size:19px}

/* testimonial */
.testimonials{left:0;top:2238px;width:1200px;height:347px;background:var(--green);color:var(--white);text-align:center}
.testimonials h2{position:absolute;left:0;top:40px;width:1200px;font-family:"Raleway",sans-serif;font-weight:400;font-size:27px;letter-spacing:2px}
.reader-photo{position:absolute;left:561px;top:88px;width:78px;height:78px;border-radius:50%;background:radial-gradient(circle,#e8ddd6,#c9b6a9 70%,#f3f3f3);border:3px solid var(--white)}
.quote-rule{position:absolute;left:154px;width:888px;height:1px;background:rgba(255,255,255,.75)}
.quote{position:absolute;left:0;top:210px;width:1200px;font-family:"Raleway",sans-serif;font-size:17px;letter-spacing:.8px}
.quote-author{position:absolute;left:0;top:254px;width:1200px;font-style:italic;font-size:16px;letter-spacing:.5px}

/* footer */
.footer-brand{left:93px;top:2672px;display:flex;align-items:center;gap:8px}
.footer-brand .brand-name{font-size:22px}
.footer-brand .brand-dot{width:10px;height:10px}
.footer-phone{left:135px;top:2752px;font-size:14px;font-weight:bold;display:flex;align-items:center;gap:10px;color:var(--ink)}
.footer-divider{top:2624px;width:1px;height:154px;background:#e3e3e3}
.footer-col h3{font-weight:400;font-size:14px;color:var(--ink);margin-bottom:22px}
.footer-col li{list-style:none;font-size:11.5px;color:var(--ink);height:32px;display:flex;align-items:center;gap:16px}
.footer-col li::before{content:"\2192";color:var(--green-dark);font-size:12px}
.social-circle{width:36px;height:36px;border-radius:50%;background:var(--green)}
.bottom-bar{left:0;top:2840px;width:1200px;height:54px;background:var(--footer-bar);color:#ddd;font-size:11px;display:flex;align-items:center;justify-content:center}
</style>
</head>
<body>

<header class="abs site-header">
  <span class="brand-dot"></span>
  <span class="brand-name">Tidewell Gallery News</span>
</header>

<nav class="abs main-nav">
  <a href="#">HOME</a>
  <a href="#">WHAT WE DO</a>
  <a href="#">CALENDAR</a>
  <a href="#">ADVERTISE AND SUBSCRIBE</a>
  <a href="#">ARTS NEWS</a>
  <a href="#">CONTACT</a>
</nav>

<section class="abs hero-issue current" role="img" aria-label="Current issue cover: cellist in a suit playing by the bay">
  <span class="read-now">READ NOW</span>
</section>
<section class="abs hero-issue premiere" role="img" aria-label="Premiere issue cover: black and white photo of a photographer at his desk">
  <span class="read-now">READ NOW</span>
</section>
<div class="abs slider-dots"><span></span><span class="active"></span><span></span></div>

<div class="abs back-issue issue-a" role="img" aria-label="Back issue cover: premiere issue with photographer portrait"></div>
<div class="abs back-issue issue-b" role="img" aria-label="Back issue cover: actress portrait and stage performers"></div>
<div class="abs back-issue issue-c" role="img" aria-label="Back issue cover: street painting illustration in blue and orange"></div>

<a class="abs btn view-all">View All Collection</a>

<div class="abs label" style="left:85px;top:1071px">Recent Post</div>
<div class="abs label-rule" style="left:85px;top:1100px;width:677px"></div>

<article class="abs post-card feature-post">
  <div class="post-image" role="img" aria-label="Black and white photo of a surfer leaping over a wave"></div>
  <h2 class="post-title">Getting Ready For Summer</h2>
  <p class="post-meta"><span>&#9719; 23rd may 2016</span><span>&#9633; 0 comments</span></p>
  <p class="post-excerpt">Everyone is looking to lose weight these days, but most people miss the one key to just how easy it really is: eating more fiber! While you need protein, healthy fats,</p>
  <a class="btn">Read More</a>
</article>

<aside class="abs about-panel">
  <div class="label">What We Do</div>
  <div class="label-rule"></div>
  <div class="abs about-photo" role="img" aria-label="Portrait of the editor holding a rose"></div>
  <p class="abs about-text">And so we begin with Tidewell Gallery News, an online magazine written for Tidewell readers and their friends who love the Arts.</p>
  <a class="abs outline-btn">Read More</a>
  <div class="abs about-social"><span></span><span></span><span></span><span></span></div>
</aside>

<article class="abs post-card small-post one">
  <div class="post-image" role="img" aria-label="Country road under a stormy sky"></div>
  <h2 class="post-title">Getting Ready For Summer</h2>
  <p class="post-meta"><span>&#9719; 23rd may 2016</span><span>&#9633; 0 comments</span></p>
  <p class="post-excerpt">Everyone is looking to lose weight these days, but most people miss the one key to just how easy it</p>
  <a class="btn">Read More</a>
</article>

<article class="abs post-card small-post two">
  <div class="post-image" role="img" aria-label="Blue sea and sky with swimmers"></div>
  <h2 class="post-title">Getting Ready For Summer</h2>
  <p class="post-meta"><span>&#9719; 23rd may 2016</span><span>&#9633; 0 comments</span></p>
  <p class="post-excerpt">Everyone is looking to lose weight these days, but most people miss the one key to just how easy it</p>
  <a class="btn">Read More</a>
</article>

<section class="abs newsletter" role="img" aria-label="Dark wooden desk background">
  <div class="newsletter-frame"></div>
  <h2 class="newsletter-title">Subscribe To<br>The Newsletter</h2>
  <div class="newsletter-rule"></div>
  <p class="newsletter-text">Get The Latest Fashion Trends From Our Handpicked Designers Straight Into Your Email Inbox!</p>
  <div class="email-field">Enter Your Email ID....</div>
  <a class="btn">Subscribe</a>
</section>

<section class="abs testimonials">
  <h2>WHAT THE READER SAY</h2>
  <div class="reader-photo" role="img" aria-label="Reader portrait"></div>
  <div class="quote-rule" style="top:179px"></div>
  <p class="quote">"It takes on average 150 hours of development to deliver 1 hr of training at $6,000!"</p>
  <p class="quote-author">Halvorsen Group</p>
  <div class="quote-rule" style="top:295px"></div>
</section>

<footer>
  <div class="abs footer-brand"><span class="brand-dot"></span><span class="brand-name">Tidewell Gallery News</span></div>
  <div class="abs footer-phone">
    <svg width="14" height="14" viewBox="0 0 24 24"><path fill="#5fb77d" d="M6.6 10.8a15 15 0 0 0 6.6 6.6l2.2-2.2c.3-.3.7-.4 1-.2 1.1.4 2.3.6 3.6.6.6 0 1 .4 1 1V20c0 .6-.4 1-1 1A17 17 0 0 1 3 4c0-.6.4-1 1-1h3.5c.6 0 1 .4 1 1 0 1.3.2 2.5.6 3.6.1.3 0 .7-.2 1z"/></svg>
    555-014-0745
  </div>
  <div class="abs footer-divider" style="left:311px"></div>
  <div class="abs footer-col" style="left:401px;top:2668px">
    <h3>Quick Links</h3>
    <ul><li>Home</li><li>Help Center</li></ul>
  </div>
  <div class="abs footer-divider" style="left:558px"></div>
  <div class="abs footer-col" style="left:666px;top:2668px">
    <h3>Company</h3>
    <ul><li>Contact</li><li>Privacy Policy</li><li>Terms of Service</li></ul>
  </div>
  <div class="abs footer-divider" style="left:826px"></div>
  <span class="abs social-circle" style="left:924px;top:2685px"></span>
  <span class="abs social-circle" style="left:983px;top:2685px"></span>
  <span class="abs social-circle" style="left:924px;top:2737px"></span>
  <span class="abs social-circle" style="left:983px;top:2737px"></span>
  <div class="abs bottom-bar">tidewellgallerynews.example 2017. All rights reserved</div>
</footer>

</body>
</html>
```